Brightmend Outdoor Signage

We need an outdoor signage design for my company with new logo designed from artflockhub. We do electrical, Air conditioning & Plumbing, installation, service, repairs and maintenance. The design shall be an eye catching that cannot miss ready it.

Industry/Entity Type

Electrical, Air conditioning, Plumbing

```html
<!DOCTYPE html>
<html lang="en">
<head>
<meta charset="utf-8">
<title>Brightmend Outdoor Signage</title>
<link href="https://fonts.googleapis.com/css2?family=Anton&family=Montserrat:wght@600;700;800&display=swap" rel="stylesheet">
<style>
  :root {
    --blue: #1f63b4;
    --blue-deep: #174f98;
    --blue-photo: #4a7fc4;
    --blue-figure: #2c68bd;
    --orange: #ee8431;
    --red: #d8262c;
    --ink: #111111;
    --white: #ffffff;
    --page: #ffffff;
  }
  * { margin: 0; padding: 0; box-sizing: border-box; }
  html, body { width: 1200px; height: 1010px; overflow: hidden; background: var(--page); }
  .canvas { position: relative; width: 1200px; height: 1010px; }
  .sign {
    position: absolute; left: 138px; top: 298px; width: 929px; height: 464px;
    background: var(--white); overflow: hidden;
  }
  .sign-blue {
    position: absolute; inset: 0;
    background: var(--blue);
    clip-path: polygon(0 0, 549px 0, 460px 368px, 347px 464px, 0 464px);
  }
  .work-photo {
    position: absolute; left: 0; top: 0; width: 560px; height: 170px;
    background: linear-gradient(180deg, var(--blue-photo) 0%, rgba(74,127,196,0.6) 60%, rgba(31,99,180,0) 100%);
    clip-path: polygon(0 0, 549px 0, 508px 170px, 0 170px);
  }
  .technician-photo {
    position: absolute; left: 430px; top: 35px; width: 180px; height: 333px;
    background: linear-gradient(180deg, rgba(44,104,189,0.35) 0%, var(--blue-figure) 100%);
  }
  .headline {
    position: absolute; left: 50px; top: 150px;
    font-family: "Anton", "Impact", sans-serif; font-size: 82px; line-height: 82px;
    color: var(--white); letter-spacing: 1px;
    transform: scaleY(1.05); transform-origin: top left;
  }
  .headline .accent { color: var(--orange); }
  .brand {
    position: absolute; left: 672px; top: 44px; width: 150px; text-align: center;
    font-family: "Montserrat", sans-serif;
  }
  .brand-dot {
    width: 54px; height: 54px; border-radius: 50%; background: var(--orange);
    margin: 0 auto 12px;
  }
  .brand-name { font-size: 24px; font-weight: 700; color: var(--orange); line-height: 30px; }
  .brand-tagline { font-size: 7.5px; font-weight: 700; color: var(--ink); margin-top: 1px; }
  .services {
    position: absolute; left: 676px; top: 182px; list-style: none;
    font-family: "Montserrat", sans-serif; font-weight: 700; font-size: 17.5px;
    color: var(--ink); letter-spacing: 0.5px;
  }
  .services li { display: flex; align-items: center; height: 28px; }
  .services svg { width: 18px; height: 18px; margin-right: 4px; flex: none; }
  .call-band {
    position: absolute; left: 0; top: 368px; width: 929px; height: 96px;
    background: var(--orange);
    clip-path: polygon(390px 0, 929px 0, 929px 96px, 347px 96px);
  }
  .bottom-strip {
    position: absolute; left: 0; top: 457px; width: 929px; height: 7px;
    background: var(--orange);
  }
  .call {
    position: absolute; left: 414px; top: 383px; display: flex; align-items: center;
    font-family: "Montserrat", sans-serif; font-weight: 800; font-size: 57px;
    color: var(--white); line-height: 66px;
  }
  .call svg { width: 38px; height: 38px; margin-right: 15px; }
</style>
</head>
<body>
<div class="canvas">
  <section class="sign">
    <div class="sign-blue"></div>
    <div class="work-photo" role="img" aria-label="Photo of a plumber's hands fitting a tap on a wall pipe, tinted blue"></div>
    <div class="technician-photo" role="img" aria-label="Photo of a smiling technician in a hard hat and overalls holding a wrench"></div>

    <h1 class="headline"><span class="accent">NEED A</span><br>PLUMBING<br>EXPERT ?</h1>

    <div class="brand">
      <div class="brand-dot"></div>
      <div class="brand-name">Brightmend</div>
      <div class="brand-tagline">Electrical&nbsp; Air Conditioning&nbsp; Plumbing</div>
    </div>

    <ul class="services">
      <li><svg viewBox="0 0 20 20"><circle cx="10" cy="10" r="8.5" fill="none" stroke="#d8262c" stroke-width="1.8"/><path d="M6 10.3l2.7 2.6L14 7.5" fill="none" stroke="#d8262c" stroke-width="1.8" stroke-linecap="round" stroke-linejoin="round"/></svg>&nbsp;&nbsp;ELECTRICAL,</li>
      <li><svg viewBox="0 0 20 20"><circle cx="10" cy="10" r="8.5" fill="none" stroke="#d8262c" stroke-width="1.8"/><path d="M6 10.3l2.7 2.6L14 7.5" fill="none" stroke="#d8262c" stroke-width="1.8" stroke-linecap="round" stroke-linejoin="round"/></svg>&nbsp;&nbsp;AIR CONDITIONING</li>
      <li><svg viewBox="0 0 20 20"><circle cx="10" cy="10" r="8.5" fill="none" stroke="#d8262c" stroke-width="1.8"/><path d="M6 10.3l2.7 2.6L14 7.5" fill="none" stroke="#d8262c" stroke-width="1.8" stroke-linecap="round" stroke-linejoin="round"/></svg>&nbsp;&nbsp;PLUMBING,</li>
      <li><svg viewBox="0 0 20 20"><circle cx="10" cy="10" r="8.5" fill="none" stroke="#d8262c" stroke-width="1.8"/><path d="M6 10.3l2.7 2.6L14 7.5" fill="none" stroke="#d8262c" stroke-width="1.8" stroke-linecap="round" stroke-linejoin="round"/></svg>&nbsp;&nbsp;INSTALLATION,</li>
      <li><svg viewBox="0 0 20 20"><circle cx="10" cy="10" r="8.5" fill="none" stroke="#d8262c" stroke-width="1.8"/><path d="M6 10.3l2.7 2.6L14 7.5" fill="none" stroke="#d8262c" stroke-width="1.8" stroke-linecap="round" stroke-linejoin="round"/></svg>&nbsp;&nbsp;REPAIRS AND</li>
      <li><svg viewBox="0 0 20 20"><circle cx="10" cy="10" r="8.5" fill="none" stroke="#d8262c" stroke-width="1.8"/><path d="M6 10.3l2.7 2.6L14 7.5" fill="none" stroke="#d8262c" stroke-width="1.8" stroke-linecap="round" stroke-linejoin="round"/></svg>&nbsp;&nbsp;MAINTENANCE.</li>
    </ul>

    <div class="call-band"></div>
    <div class="bottom-strip"></div>
    <div class="call">
      <svg viewBox="0 0 24 24"><path d="M6.6 2.5l3 3.6c.4.5.4 1.2-.1 1.7L8 9.3c1.2 2.6 3.9 5.3 6.7 6.7l1.5-1.5c.5-.5 1.2-.5 1.7-.1l3.6 3c.5.4.6 1.2.1 1.7l-2 2.2c-.6.6-1.5.8-2.3.5C9.6 19.4 4.6 14.4 2.2 6.7c-.3-.8-.1-1.7.5-2.3l2.2-2c.5-.4 1.3-.4 1.7.1z" fill="#c41f26"/><path d="M14 3.5a6.5 6.5 0 0 1 6.5 6.5M14 6.8a3.2 3.2 0 0 1 3.2 3.2" fill="none" stroke="#c41f26" stroke-width="1.8" stroke-linecap="round"/></svg>
      +1555019284
    </div>
  </section>
</div>
</body>
</html>
```